Design a menu for health restaurant

A health food restaurant in Los Angeles is seeking menu design. Our foods are made from scratch using whole ingredients.
Name: Grubb Larder
Address: 1000 E 60th StLos Angeles, CA 90247
Website: www.GrubbLarder.example
We are looking for a clean and simple menu. Brand colors are white/tan, green and orange.

Please see attached excel with menu items and logo. We do not yet have prices.

Colors
f78f20
9bcb3c
ffffff
fff3d1

Requirements
Must have
• Easy to read.
Trifold menu design (front and back).
VEGAN, VEGETARIAN, GLUTEN FREE, CONTAINS NUTS symbols.
Logo.
Nice to have
• Incorporate brand colors, but still be easy to read.
We would like to use the Belco font (attached) if it works. If not we are open to a similar font that is easy to read.

Please see attached images.
We like the images and headers of OPTION 1. Would like something similar in trifold format.
We like the clean fonts of OPTION 2.

```html
<!DOCTYPE html>
<html lang="en">
<head>
<meta charset="utf-8">
<title>Grubb Larder Menu</title>
<link rel="stylesheet" href="https://fonts.googleapis.com/css2?family=Didact+Gothic&family=Fredoka:wght@600&display=swap">
<style>
:root{
  --cream:#fff3d1;
  --orange:#f78f20;
  --lime:#9bcb3c;
  --green:#2e9c46;
  --green-dark:#1f7a36;
  --nut:#a23a32;
  --ink:#1d1d1b;
  --white:#ffffff;
}
*{margin:0;padding:0;box-sizing:border-box}
html,body{width:1200px;height:517px;overflow:hidden;background:var(--cream)}
.menu{position:relative;width:1200px;height:517px;background:var(--cream);font-family:"Didact Gothic",sans-serif;color:var(--ink)}
.section{position:absolute;width:333px}
.section-title{
  position:relative;height:15px;background:var(--orange);
  border-bottom:2px solid var(--lime);margin-bottom:14px;
}
.section-title h2{
  position:absolute;left:3px;top:-2px;
  font-family:"Fredoka",sans-serif;font-weight:600;font-size:18px;line-height:20px;
  letter-spacing:.5px;color:var(--white);-webkit-text-stroke:1px var(--ink);paint-order:stroke fill;
}
.item{margin-bottom:6px}
.item-head{display:flex;justify-content:space-between;align-items:baseline;font-size:11px;line-height:13px}
.item-name{display:flex;align-items:center;gap:5px}
.tags{display:inline-flex;gap:2px;font-family:"Fredoka",sans-serif;font-size:7px;line-height:8px}
.tag{padding:0 1px;border:.6px solid currentColor;border-radius:2px;background:var(--white)}
.tag-v{color:var(--orange)}
.tag-gf{color:var(--green-dark)}
.tag-n{color:var(--nut)}
.tag-veg{color:var(--lime)}
.item-desc{font-size:6px;line-height:8px;max-width:280px}
.drinks{left:33px;top:33px}
.smoothies{left:33px;top:349px}
.snacks{left:433px;top:33px}
.desserts{left:433px;top:190px}
.legend{
  position:absolute;left:433px;top:461px;width:333px;height:22px;background:var(--white);
  display:flex;align-items:center;justify-content:center;gap:6px;font-size:10.5px;
}
.legend .tag{font-size:8px}
.cover{position:absolute;left:799px;top:0;width:401px;height:517px}
.cover-art{position:absolute;left:0;top:0}
.brand{
  position:absolute;left:1003px;top:205px;width:130px;height:130px;border-radius:50%;
  background:var(--white);border:3px solid var(--orange);
  display:flex;align-items:center;justify-content:center;
  font-size:16px;color:var(--green);text-align:center;line-height:20px;
}
.cover-band{position:absolute;left:941px;top:401px;width:259px;height:30px;background:var(--orange);border-bottom:2px solid var(--lime)}
.cover-title{
  position:absolute;left:1003px;top:397px;font-family:"Fredoka",sans-serif;font-weight:600;
  font-size:44px;line-height:44px;letter-spacing:2px;color:var(--white);
  -webkit-text-stroke:1.5px var(--ink);paint-order:stroke fill;
}
</style>
</head>
<body>
<main class="menu">

  <section class="section drinks">
    <div class="section-title"><h2>DRINKS</h2></div>
    <div class="item"><div class="item-head"><span class="item-name">Coffee</span><span>$0.00</span></div><p class="item-desc">We proudly serve Tidewater Coffee, a local roaster.</p></div>
    <div class="item"><div class="item-head"><span class="item-name">Power Date Shake <span class="tags"><span class="tag tag-v">V</span><span class="tag tag-gf">GF</span></span></span><span>$0.00</span></div><p class="item-desc">Ice-blended energy smoothie featuring dates and coffee.</p></div>
    <div class="item"><div class="item-head"><span class="item-name">Heart Beet Juice <span class="tags"><span class="tag tag-v">V</span><span class="tag tag-gf">GF</span></span></span><span>$0.00</span></div><p class="item-desc">Red beet, apple, carrot, ginger, parsley, and lemon.</p></div>
    <div class="item"><div class="item-head"><span class="item-name">Green Leafy Juice <span class="tags"><span class="tag tag-v">V</span><span class="tag tag-gf">GF</span></span></span><span>$0.00</span></div><p class="item-desc">Spinach, kale, cucumber, apple, and oranges.</p></div>
    <div class="item"><div class="item-head"><span class="item-name">Orange Turmeric Juice <span class="tags"><span class="tag tag-v">V</span><span class="tag tag-gf">GF</span></span></span><span>$0.00</span></div><p class="item-desc">Turmeric, ginger, lemon, carrot, and orange topped with cracked black pepper.</p></div>
    <div class="item"><div class="item-head"><span class="item-name">Fireshot <span class="tags"><span class="tag tag-v">V</span><span class="tag tag-gf">GF</span></span></span><span>$0.00</span></div><p class="item-desc">Ginger and lemon shot topped with cayenne.</p></div>
    <div class="item"><div class="item-head"><span class="item-name">Lemonade</span><span>$0.00</span></div><p class="item-desc">House Made Lemonade. Choice of unsweetened or agave sweetened in Regular, Raspberry, and Lavender flavors.</p></div>
    <div class="item"><div class="item-head"><span class="item-name">Tea</span><span>$0.00</span></div><p class="item-desc">Hot or iced.</p></div>
    <div class="item"><div class="item-head"><span class="item-name">Bottled Drinks</span><span>$0.00</span></div><p class="item-desc">Brightleaf kombucha (Harmony Trio, Harmony Gingerberry, Harmony Mango)<br>Fizzbrook (Orange Mango, Lemon, Grapefruit)<br>Palmgrove Coconut Original<br>Sparkling Water (Clearspring)<br>Still Water (Clearspring)</p></div>
  </section>

  <section class="section smoothies">
    <div class="section-title"><h2>SMOOTHIES</h2></div>
    <div class="item"><div class="item-head"><span class="item-name">Green Machine Smoothie <span class="tags"><span class="tag tag-veg">VEG</span><span class="tag tag-gf">GF</span><span class="tag tag-n">N</span></span></span><span>$0.00</span></div><p class="item-desc">Romaine, spinach, banana, mango, pineapple, flaxmilk, spirulina, almond butter</p></div>
    <div class="item"><div class="item-head"><span class="item-name">Acai Smoothie <span class="tags"><span class="tag tag-veg">VEG</span><span class="tag tag-gf">GF</span><span class="tag tag-n">N</span></span></span><span>$0.00</span></div><p class="item-desc">Acai, blueberries, banana, pineapple, Macqui berry, flaxmilk, almond butter</p></div>
    <div class="item"><div class="item-head"><span class="item-name">Mango Smoothie <span class="tags"><span class="tag tag-v">V</span><span class="tag tag-gf">GF</span></span></span><span>$0.00</span></div><p class="item-desc">Mango, flaxmilk, banan, hemp seeds</p></div>
  </section>

  <section class="section snacks">
    <div class="section-title"><h2>SNACKS N’ SIDES</h2></div>
    <div class="item"><div class="item-head"><span class="item-name">Fries <span class="tags"><span class="tag tag-v">V</span><span class="tag tag-gf">GF</span></span></span><span>$0.00</span></div><p class="item-desc" style="max-width:320px">Hand cut air-fries with house seasonings. Choose regular or sweet potato fries.<br>Guacamole with blue corn tortilla chips.<br>Hummus with blue corn tortilla chips.</p></div>
    <div class="item"><div class="item-head"><span class="item-name">Side Salad</span><span>$0.00</span></div><p class="item-desc" style="max-width:320px">Your choice of House, Golden Beet, Mediterranean, or Vegan Chef side salad. (24oz)</p></div>
    <div class="item"><div class="item-head"><span class="item-name">Guac + Chips <span class="tags"><span class="tag tag-v">V</span><span class="tag tag-gf">GF</span></span></span><span>$0.00</span></div><p class="item-desc" style="max-width:320px">Your choice of House, Golden Beet, Mediterranean, or Vegan Chef side salad. (24oz)</p></div>
    <div class="item"><div class="item-head"><span class="item-name">Hummus + Chips <span class="tags"><span class="tag tag-v">V</span><span class="tag tag-gf">GF</span></span></span><span>$0.00</span></div><p class="item-desc" style="max-width:320px">Your choice of House, Golden Beet, Mediterranean, or Vegan Chef side salad. (24oz)</p></div>
  </section>

  <section class="section desserts">
    <div class="section-title"><h2>DESSERTS</h2></div>
    <div class="item"><div class="item-head"><span class="item-name">Date Coffee Cake <span class="tags"><span class="tag tag-v">V</span><span class="tag tag-n">N</span></span></span><span>$0.00</span></div><p class="item-desc">Signature date coffee cake with walnuts.</p></div>
    <div class="item"><div class="item-head"><span class="item-name">Fruit + Spices <span class="tags"><span class="tag tag-v">V</span><span class="tag tag-gf">GF</span></span></span><span>$0.00</span></div><p class="item-desc" style="max-width:320px">Strawberry, pineapple, green apple, orange, and blueberries with lime and chili seasoning.</p></div>
    <div class="item"><div class="item-head"><span class="item-name">Cookies <span class="tags"><span class="tag tag-veg">VEG</span></span></span><span>$0.00</span></div><p class="item-desc">Your choice of Chocolate Chip or Double Chocolate Chip fresh baked cookie.</p></div>
    <div class="item"><div class="item-head"><span class="item-name">Larder Chocolate Mousse <span class="tags"><span class="tag tag-v">V</span><span class="tag tag-gf">GF</span></span></span><span>$0.00</span></div><p class="item-desc">Served with grated dark chocolate.</p></div>
  </section>

  <div class="legend">
    <span class="tags"><span class="tag tag-veg">VEG</span></span>Vegetarian •
    <span class="tags"><span class="tag tag-v">V</span></span>Vegan •
    <span class="tags"><span class="tag tag-n">N</span></span>Contains Nuts •
    <span class="tags"><span class="tag tag-gf">GF</span></span>Gluten Free
  </div>

  <div class="cover">
    <svg class="cover-art" width="401" height="517" viewBox="0 0 401 517">
      <defs>
        <linearGradient id="gingham" x1="0" y1="0" x2="1" y2="1">
          <stop offset="0" stop-color="#3aa64f"/>
          <stop offset="1" stop-color="#6fbf72"/>
        </linearGradient>
      </defs>
      <rect width="401" height="517" fill="#fbeecb" opacity=".5" role="img" aria-label="Faint line drawings of vegetables and fruit"/>
      <polygon points="377,0 401,0 401,513 142,259" fill="url(#gingham)" role="img" aria-label="Green and white gingham tablecloth pattern"/>
    </svg>
  </div>

  <div class="brand">Grubb<br>Larder</div>
  <div class="cover-band"></div>
  <div class="cover-title">MENU</div>

</main>
</body>
</html>
```